Business card, postcard, pocket folder

We are a real estate team and have had a new logo designed. From this, we need the following deliverables:- Business Cards (double-sided)- Just Listed / Just Sold Postcards (double-sided)- Pocket Folder. See logo attached.More work possible for the winning designer.
There are 5 members of the team, so head shots should be easily changed and possible for a group photo might be a good idea for the pocket folder but not 100% neccessary.
Target Market(s)
Real estate
Industry/Entity Type
Real Estate
Font styles to use
Serif
Sans Serif
Requirements
Must have
- Business cards and postcards must have a head shot on them.

```html
<!DOCTYPE html>
<html lang="en">
<head>
<meta charset="utf-8">
<title>Harrowgate Group – Business Card</title>
<link rel="stylesheet" href="https://fonts.googleapis.com/css2?family=Open+Sans:wght@400;600;700&display=swap">
<style>
  :root {
    --brand-blue: #2435a0;
    --accent-red: #e5202e;
    --ink-grey: #555a60;
    --paper: #ffffff;
    --stage: #e9e9ec;
    --photo-dark: #3a3b38;
    --photo-mid: #5a5b57;
  }
  * { box-sizing: border-box; margin: 0; padding: 0; }
  html, body {
    width: 1200px; height: 959px; overflow: hidden;
    background: var(--stage);
    font-family: "Open Sans", Arial, sans-serif;
  }
  .canvas { position: relative; width: 1200px; height: 959px; }

  .card {
    position: absolute; left: 270px;
    width: 660px; height: 377px;
    overflow: hidden;
    box-shadow: 0 6px 18px rgba(0,0,0,.18);
  }

  /* Back side */
  .card-back { top: 62px; background: var(--brand-blue); color: var(--paper); }
  .card-back .brand {
    position: absolute; right: 60px; bottom: 118px;
    font-size: 46px; font-weight: 700; letter-spacing: -0.5px; line-height: 1;
  }
  .card-back .website {
    position: absolute; right: 62px; bottom: 78px;
    font-size: 17px; letter-spacing: 4px;
  }

  /* Front side */
  .card-front { top: 520px; background: var(--paper); }
  .headshot {
    position: absolute; left: 0; top: 0; width: 330px; height: 282px;
    background: linear-gradient(180deg, var(--photo-mid), var(--photo-dark));
  }
  .contact-band {
    position: absolute; left: 0; right: 0; top: 282px; height: 44px;
    background: var(--brand-blue); color: var(--paper);
    display: flex; align-items: center; padding-left: 22px;
    font-size: 15px; white-space: nowrap;
  }
  .contact-band b { font-weight: 700; margin-right: 4px; }
  .contact-band span { margin-right: 12px; }

  .brand-mark {
    position: absolute; right: 60px; top: 58px;
    width: 250px; text-align: right;
    color: var(--brand-blue);
    font-size: 38px; font-weight: 700; letter-spacing: -0.5px; line-height: 1.02;
  }
  .person { position: absolute; right: 60px; top: 158px; text-align: right; }
  .person .name { color: var(--brand-blue); font-weight: 700; font-size: 21px; line-height: 1.1; }
  .person .role { color: var(--accent-red); font-size: 16px; line-height: 1.2; }
  .address {
    position: absolute; left: 372px; top: 212px;
    color: var(--ink-grey); font-size: 15px; line-height: 1.35;
    font-style: normal;
  }
</style>
</head>
<body>
<main class="canvas">
  <section class="card card-back" aria-label="Business card back">
    <div class="brand">Harrowgate Group</div>
    <div class="website">www.harrowgategroup.com</div>
  </section>

  <section class="card card-front" aria-label="Business card front">
    <div class="headshot" role="img" aria-label="Agent head shot photo"></div>
    <div class="brand-mark">Harrowgate<br>Group</div>
    <div class="person">
      <div class="name">MARK ELLISON</div>
      <div class="role">PRESIDENT</div>
    </div>
    <address class="address">
      2190 Alder Crest Lane<br>
      Brookhaven, NY 11719
    </address>
    <div class="contact-band">
      <span><b>P:</b>555 0142 7781</span>
      <span><b>M:</b>555 0198 3364</span>
      <span><b>E:</b>mark@harrowgategroup.com</span>
    </div>
  </section>
</main>
</body>
</html>
```